New bussiness card, using company logo.
Gerald Finch
Manager/Director
Finch Property Developments
Po Box 4637
Thuringowa Central
Qld
0412 558 306
gerald@finchpropertydevelopments
eye catching, vibrant colours, professional

It Company

```html
<!DOCTYPE html>
<html lang="en">
<head>
<meta charset="utf-8">
<title>Finch Property Developments – Business Card</title>
<link rel="stylesheet" href="https://fonts.googleapis.com/css2?family=Exo+2:wght@700;800&family=Ubuntu:wght@400;500;700&display=swap">
<style>
  :root {
    --page-bg: #e9eaec;
    --green: #7cc242;
    --green-dark: #4f9a23;
    --green-light: #b5e08a;
    --panel-top: #ffffff;
    --panel-bottom: #c9cacc;
    --panel-edge: #4a4b4d;
    --red: #c8262c;
    --grey-text: #5d5e60;
    --pill: #2a2b2d;
    --pill-text: #ffffff;
  }
  * { box-sizing: border-box; margin: 0; padding: 0; }
  html, body { width: 1200px; height: 861px; overflow: hidden; }
  body {
    background: var(--page-bg);
    font-family: "Ubuntu", sans-serif;
    position: relative;
  }
  .card {
    position: absolute;
    top: 262px;
    width: 520px;
    height: 330px;
    padding: 34px 30px;
    background: linear-gradient(160deg, var(--green-light), var(--green) 55%, var(--green-dark));
    box-shadow: 0 14px 30px rgba(0,0,0,.18);
  }
  .card--front { left: 58px; }
  .card--back { left: 622px; }
  .card__panel {
    width: 100%;
    height: 100%;
    border: 3px solid var(--panel-edge);
    background: linear-gradient(180deg, var(--panel-top) 0%, #f1f1f2 45%, var(--panel-bottom) 100%);
    display: flex;
    flex-direction: column;
    align-items: center;
    justify-content: center;
  }
  .brand {
    display: flex;
    align-items: center;
    gap: 14px;
  }
  .brand__mark {
    width: 28px;
    height: 28px;
    background: var(--green);
  }
  .brand__name {
    font-family: "Ubuntu", sans-serif;
    font-weight: 700;
    font-size: 30px;
    line-height: 1.1;
    color: var(--red);
    letter-spacing: .5px;
    text-transform: uppercase;
  }
  .person__name {
    font-family: "Exo 2", sans-serif;
    font-weight: 800;
    font-size: 38px;
    color: var(--red);
    letter-spacing: 1px;
    text-transform: uppercase;
    line-height: 1;
  }
  .person__role {
    margin-top: 6px;
    font-weight: 700;
    font-size: 14px;
    color: var(--grey-text);
    letter-spacing: .6px;
    text-transform: uppercase;
  }
  .contacts {
    list-style: none;
    margin-top: 28px;
    display: flex;
    flex-direction: column;
    align-items: center;
    gap: 10px;
  }
  .contact {
    display: flex;
    align-items: center;
    gap: 8px;
    height: 26px;
    padding: 0 3px;
    border-radius: 13px;
    background: var(--pill);
    color: var(--pill-text);
    font-size: 16px;
    white-space: nowrap;
  }
  .contact__icon {
    width: 21px;
    height: 21px;
    border-radius: 50%;
    background: var(--green);
    border: 2px solid #d8f0c0;
    display: flex;
    align-items: center;
    justify-content: center;
    flex: none;
  }
  .contact__icon svg { width: 11px; height: 11px; fill: var(--pill); }
</style>
</head>
<body>
  <section class="card card--front" aria-label="Card front">
    <div class="card__panel">
      <div class="brand">
        <span class="brand__mark"></span>
        <span class="brand__name">Finch Property<br>Developments</span>
      </div>
    </div>
  </section>

  <section class="card card--back" aria-label="Card back">
    <div class="card__panel">
      <h1 class="person__name">Gerald Finch</h1>
      <p class="person__role">Manager/Director</p>
      <ul class="contacts">
        <li class="contact">
          <span class="contact__icon"><svg viewBox="0 0 12 12"><path d="M6 0a4 4 0 0 0-4 4c0 3 4 8 4 8s4-5 4-8a4 4 0 0 0-4-4zm0 5.5A1.5 1.5 0 1 1 6 2.5a1.5 1.5 0 0 1 0 3z"/></svg></span>
          Po Box 4637, Harlow Vale, NSW
          <span class="contact__icon"><svg viewBox="0 0 12 12"><path d="M6 0a4 4 0 0 0-4 4c0 3 4 8 4 8s4-5 4-8a4 4 0 0 0-4-4zm0 5.5A1.5 1.5 0 1 1 6 2.5a1.5 1.5 0 0 1 0 3z"/></svg></span>
        </li>
        <li class="contact">
          <span class="contact__icon"><svg viewBox="0 0 12 12"><path d="M2.5 0.5l2 2.5-1.2 1.3c.8 1.6 2 2.8 3.4 3.6L8 6.6l2.5 2-1 2.4C5 10.6 1.4 7 1 2.5z"/></svg></span>
          0412 558 306
          <span class="contact__icon"><svg viewBox="0 0 12 12"><path d="M2.5 0.5l2 2.5-1.2 1.3c.8 1.6 2 2.8 3.4 3.6L8 6.6l2.5 2-1 2.4C5 10.6 1.4 7 1 2.5z"/></svg></span>
        </li>
        <li class="contact">
          <span class="contact__icon"><svg viewBox="0 0 12 12"><path d="M0 2h12v1L6 7 0 3zm0 2.5l6 4 6-4V10H0z"/></svg></span>
          gerald@finchpropertydevelopments
          <span class="contact__icon"><svg viewBox="0 0 12 12"><path d="M0 2h12v1L6 7 0 3zm0 2.5l6 4 6-4V10H0z"/></svg></span>
        </li>
      </ul>
    </div>
  </section>
</body>
</html>
```